Webpage

I am a professional genealogist. I need a webpage that is professional looking (using the logo I chose), I can add hyperlinks and photos to if and when I want.

```html
<!DOCTYPE html>
<html lang="en">
<head>
<meta charset="utf-8">
<title>Kinward Research Services</title>
<link href="https://fonts.googleapis.com/css2?family=Open+Sans:wght@400;600;700&display=swap" rel="stylesheet">
<style>
:root{
  --green:#7dbb9a;
  --green-text:#6bb08d;
  --green-deep:#4a8a6b;
  --ink:#2a2a2a;
  --muted:#666;
  --panel:#eeeeee;
  --white:#ffffff;
  --field:#8a8a8a;
  --line:#d4d4d4;
}
html,body{margin:0;padding:0;overflow:hidden;background:var(--white);}
.page{position:relative;width:1036px;height:1200px;overflow:hidden;font-family:'Open Sans',sans-serif;color:var(--ink);background:var(--panel);}
.abs{position:absolute;}

/* header */
.site-header{position:absolute;left:0;top:0;width:1036px;height:74px;background:var(--white);box-shadow:0 1px 3px rgba(0,0,0,.08);z-index:2;}
.brand{position:absolute;left:146px;top:18px;display:flex;align-items:center;gap:8px;}
.brand-dot{width:34px;height:34px;border-radius:50%;background:var(--green);}
.brand-name{font-size:12px;font-weight:400;color:var(--ink);line-height:1.1;}
.main-nav a{position:absolute;top:31px;font-size:10px;letter-spacing:.3px;color:var(--green-text);text-decoration:none;}
.main-nav .active::after{content:"";position:absolute;left:-6px;right:-6px;top:39px;height:3px;background:var(--green);}

/* hero */
.hero{position:absolute;left:0;top:74px;width:1036px;height:346px;background:linear-gradient(120deg,#cfe2b9 0%,#eef3e6 40%,#f4f2ea 60%,#c9ddb0 100%);}
.hero-title{position:absolute;left:381px;top:194px;margin:0;font-size:37px;line-height:35px;font-weight:700;color:var(--ink);}
.hero-title span{color:var(--green);}
.slider-dots{position:absolute;top:305px;left:522px;display:flex;gap:6px;}
.slider-dots i{width:14px;height:14px;border-radius:50%;background:var(--green);display:block;}
.slider-dots i.on{background:#444;}

/* bio */
.bio{position:absolute;left:0;top:420px;width:1036px;height:198px;background:var(--panel);border-bottom:1px solid #ddd;}
.portrait{position:absolute;left:146px;top:44px;width:106px;height:106px;border-radius:50%;border:6px solid var(--green);background:linear-gradient(#9aa2a6,#6e7679);}
.bio h2{position:absolute;left:289px;top:44px;margin:0;font-size:25px;font-weight:600;letter-spacing:.3px;}
.bio p{position:absolute;left:289px;top:81px;width:592px;margin:0;font-size:9.3px;line-height:11.6px;color:var(--muted);}

/* services */
.services-title{position:absolute;left:146px;top:648px;width:736px;text-align:center;font-size:25px;font-weight:600;}
.services-title::before,.services-title::after{content:"";position:absolute;top:17px;height:1px;background:var(--line);width:304px;}
.services-title::before{left:0;}
.services-title::after{right:0;}
.service{position:absolute;top:697px;width:140px;}
.service h3{margin:0 0 10px 2px;font-size:10.5px;font-weight:600;color:var(--green-text);letter-spacing:.2px;}
.service .thumb{width:140px;height:90px;}
.service .overlay{display:flex;align-items:center;justify-content:center;text-align:center;color:var(--white);font-size:10.5px;line-height:12px;padding:0 10px;box-sizing:border-box;}

/* contact */
.contact{position:absolute;left:0;top:850px;width:1036px;height:265px;background:linear-gradient(135deg,#d8d4d1,#cdccc8 50%,#d6d3cf);}
.address{position:absolute;left:160px;top:9px;width:238px;height:238px;border-radius:50%;background:var(--green);color:var(--white);}
.address h3{margin:0;position:absolute;top:50px;width:100%;text-align:center;font-size:22px;font-weight:600;color:var(--ink);}
.address ul{list-style:none;margin:0;padding:0;position:absolute;left:42px;top:105px;}
.address li{display:flex;align-items:center;gap:8px;font-size:14.5px;font-weight:600;height:27px;}
.address svg{width:16px;height:16px;}
.contact h2{position:absolute;left:565px;top:34px;margin:0;font-size:25px;font-weight:600;}
.form{position:absolute;left:562px;top:85px;width:280px;}
.field{display:block;box-sizing:border-box;width:280px;background:var(--field);border-bottom:1px solid #b9b9b9;color:var(--white);font-size:9.5px;padding:7px 12px;height:26px;}
.field.msg{height:68px;border-bottom:0;}
.send{position:absolute;left:729px;top:219px;width:112px;height:26px;background:var(--green);color:var(--white);font-size:13px;font-weight:700;text-align:center;line-height:26px;letter-spacing:.5px;}

/* footer */
.site-footer{position:absolute;left:0;top:1115px;width:1036px;height:85px;background:var(--green-deep);}
.foot-nav a{position:absolute;top:21px;font-size:9px;color:#d6ebdf;text-decoration:none;}
.copyright{position:absolute;left:147px;top:57px;font-size:9px;color:#a9d3bb;}
.foot-brand{position:absolute;left:790px;top:17px;display:flex;align-items:center;gap:6px;}
.foot-brand .brand-dot{width:30px;height:30px;background:#3b7559;}
.foot-brand .brand-name{font-size:10px;color:#1f3d2f;}
</style>
</head>
<body>
<div class="page">

  <header class="site-header">
    <div class="brand"><span class="brand-dot"></span><span class="brand-name">Kinward Research<br>Services</span></div>
    <nav class="main-nav">
      <a class="active" href="#" style="left:384px">HOME</a>
      <a href="#" style="left:454px">ABOUT</a>
      <a href="#" style="left:524px">SERVICES</a>
      <a href="#" style="left:607px">CONTACT</a>
      <a href="#" style="left:687px">PUBLICATIONS</a>
      <a href="#" style="left:792px">BLOG</a>
      <a href="#" style="left:853px">LINKS</a>
    </nav>
  </header>

  <section class="hero" role="img" aria-label="Photo of a smiling multi-generation family walking outdoors in sunlight, with a faint family tree decoration">
    <h1 class="hero-title">Duis autem vel eum <span>iriure</span><br><span>dolor</span> in hendrerit</h1>
    <div class="slider-dots"><i class="on"></i><i></i><i></i></div>
  </section>

  <section class="bio">
    <div class="portrait" role="img" aria-label="Portrait photo of the genealogist"></div>
    <h2>Dana Whitford, Professional Genealogist</h2>
    <p>Lorem ipsum dolor sit amet, consectetuer adipiscing elit, sed diam nonummy nibh euismod tincidunt ut laoreet dolore magna aliquam erat volutpat. Ut wisi enim ad minim veniam, quis nostrud exerci tation ullamcorper suscipit lobortis nisl ut aliquip ex ea commodo consequat. Duis autem vel eum iriure dolor in hendrerit in vulputate velit esse molestie consequat, vel illum dolore eu feugiat nulla facilisis at vero eros et accumsan et iusto odio dignissim qui blandit praesent luptatum zzril delenit augue duis dolore te feugait nulla facilisi.</p>
  </section>

  <h2 class="services-title">Services</h2>

  <div class="service" style="left:146px">
    <h3>Forensic Genealogy</h3>
    <div class="thumb overlay" style="background:linear-gradient(135deg,#4a3448,#2b1e2c)" role="img" aria-label="Photo of hands, with hover caption">Lorem ipsum dolor sit amet, consectetuer adipiscing elit, sed diam</div>
  </div>
  <div class="service" style="left:295px">
    <h3>Kinship Determination</h3>
    <div class="thumb" style="background:linear-gradient(135deg,#d9ecf4,#9cc6da)" role="img" aria-label="Photo of two hands forming a frame"></div>
  </div>
  <div class="service" style="left:444px">
    <h3>Research Analysis</h3>
    <div class="thumb" style="background:linear-gradient(135deg,#e9e9e9,#b8b8b8)" role="img" aria-label="Photo of people working with a laptop and documents"></div>
  </div>
  <div class="service" style="left:593px">
    <h3>Texas Researcher</h3>
    <div class="thumb" style="background:linear-gradient(180deg,#c5d3e0,#9a8a70 65%,#5b6b3c)" role="img" aria-label="Photo of a brick university building with columns"></div>
  </div>
  <div class="service" style="left:742px">
    <h3>Record Retrieval</h3>
    <div class="thumb" style="background:linear-gradient(90deg,#2e3f8a,#6fa3c7)" role="img" aria-label="Photo of stacked paper records"></div>
  </div>

  <section class="contact" role="img" aria-label="Faded street map background">
    <div class="address">
      <h3>ADDRESS</h3>
      <ul>
        <li><svg viewBox="0 0 16 16"><rect x="1" y="4" width="14" height="7" rx="1" fill="#2a2a2a"/><rect x="6" y="11" width="2" height="4" fill="#2a2a2a"/></svg>PO Box 4418</li>
        <li><svg viewBox="0 0 16 16"><path d="M8 1a5 5 0 0 0-5 5c0 4 5 9 5 9s5-5 5-9a5 5 0 0 0-5-5z" fill="none" stroke="#2a2a2a" stroke-width="1.5"/><circle cx="8" cy="6" r="1.8" fill="#2a2a2a"/></svg>Cedar Falls, TX 75500-4418</li>
        <li><svg viewBox="0 0 16 16"><path d="M2 6c0-3 12-3 12 0v1h-3V5H5v2H2z" fill="#2a2a2a"/><rect x="4" y="8" width="8" height="6" rx="1" fill="#2a2a2a"/></svg>555-014-2270</li>
        <li><svg viewBox="0 0 16 16"><rect x="1.5" y="3.5" width="13" height="9" fill="none" stroke="#2a2a2a" stroke-width="1.3"/><path d="M1.5 3.5l6.5 5 6.5-5" fill="none" stroke="#2a2a2a" stroke-width="1.3"/></svg>dana@kinward.example</li>
      </ul>
    </div>
    <h2>Contact Us</h2>
    <div class="form">
      <span class="field">Name</span>
      <span class="field">E-mail</span>
      <span class="field msg">Your Message</span>
    </div>
    <div class="send">SEND NOW</div>
  </section>

  <footer class="site-footer">
    <nav class="foot-nav">
      <a href="#" style="left:147px">HOME</a>
      <a href="#" style="left:204px">ABOUT</a>
      <a href="#" style="left:263px">SERVICES</a>
      <a href="#" style="left:333px">CONTACT</a>
      <a href="#" style="left:406px">PUBLICATIONS</a>
      <a href="#" style="left:497px">BLOG</a>
      <a href="#" style="left:550px">LINKS</a>
    </nav>
    <div class="copyright">Copyright © 2014 Kinward Research Services</div>
    <div class="foot-brand"><span class="brand-dot"></span><span class="brand-name">Kinward Research<br>Services</span></div>
  </footer>

</div>
</body>
</html>
```